Business cards for a high-end menswear store

I would like to come up with a design for our business cards.
Two different ones: one for general sales and one for the owner. It is a high-end menswear store.

Our address is: 4817 Morneau Boulevard, Montreal, QC, K7P4M2
phone number: 514-286-5937
insta: MAISONVERLAINE
Website: www.maisonverlaine.example
email (general card): info@maisonverlaine.example
email (owner): bastien@maisonverlaine.example

I have attached our logo in an ai and eps file format. You can see our old cards as well. I am looking for a modern and clean look.

Target Market(s)

High-End Clothing Market

Industry/Entity Type

Retail, Clothing, Luxury Clothing

Contact Information for Business Card

Address, Name, Email, Website, Social Info,

Font styles to use
Serif

Colors

Designer to choose colors to be used in the design.

Requirements
Must have
• Address, Name, Email, Website, Social Info,
Nice to have
• QR Code that brings you to the website

```html
<!DOCTYPE html>
<html lang="en">
<head>
<meta charset="utf-8">
<title>Maison Verlaine – Business Cards</title>
<link rel="stylesheet" href="https://fonts.googleapis.com/css2?family=Barlow:wght@400;500&display=swap">
<style>
  :root {
    --backdrop: #7a7a7a;
    --card-light: #f1eff0;
    --card-dark: #242328;
    --ink: #1c1b1d;
    --text-light: #ffffff;
    --gold-pale: #fff3a0;
    --gold-mid: #e8b33a;
    --gold-deep: #c46a0c;
  }
  * { margin: 0; padding: 0; box-sizing: border-box; }
  html, body { width: 1200px; height: 1200px; overflow: hidden; }
  body {
    position: relative;
    background: var(--backdrop);
    font-family: "Barlow", sans-serif;
  }
  .card {
    position: absolute;
    left: 237px;
    width: 726px;
    height: 402px;
    background: var(--card-light);
    box-shadow: 6px 8px 14px rgba(0,0,0,0.28);
    overflow: hidden;
  }
  .card--front { top: 150px; }
  .card--back { top: 648px; }

  .brand {
    position: absolute;
    display: flex;
    align-items: center;
    gap: 14px;
    color: var(--ink);
    font-weight: 500;
    text-transform: uppercase;
    letter-spacing: 0.22em;
    white-space: nowrap;
  }
  .brand__square {
    background: var(--ink);
    flex: none;
  }
  .card--front .brand {
    left: 50%;
    top: 150px;
    transform: translateX(-50%);
    font-size: 28px;
  }
  .card--front .brand__square { width: 34px; height: 34px; }

  .front__gold-band {
    position: absolute;
    left: 0; top: 301px;
    width: 100%; height: 11px;
    background: linear-gradient(90deg,
      var(--gold-pale) 0%, var(--gold-mid) 8%, var(--gold-deep) 15%,
      var(--gold-mid) 24%, var(--gold-pale) 50%, var(--gold-mid) 76%,
      var(--gold-deep) 85%, var(--gold-mid) 92%, var(--gold-pale) 100%);
  }
  .front__dark-band {
    position: absolute;
    left: 0; top: 312px;
    width: 100%; height: 90px;
    background: var(--card-dark);
  }

  .back__dark-panel {
    position: absolute;
    left: 363px; top: 0;
    width: 363px; height: 100%;
    background: var(--card-dark);
  }
  .card--back .brand {
    left: 181px;
    top: 188px;
    transform: translateX(-50%);
    font-size: 19px;
  }
  .card--back .brand__square { width: 24px; height: 24px; }

  .icon-rail {
    position: absolute;
    left: 345px; top: 56px;
    width: 36px; height: 289px;
    border-radius: 18px;
    background: linear-gradient(180deg,
      #fbe68e 0%, #e9b948 28%, #d8961f 42%, #f3d26a 62%,
      #fdf09a 78%, #dea232 100%);
  }
  .icon {
    position: absolute;
    left: 50%;
    width: 22px; height: 22px;
    transform: translate(-50%, -50%);
  }
  .icon--phone { top: 57px; }
  .icon--mail { top: 96px; }
  .icon--social { top: 137px; }
  .icon--link { top: 176px; }
  .icon--pin { top: 228px; }

  .contact-list {
    position: absolute;
    left: 416px; top: 0;
    list-style: none;
    color: var(--text-light);
    font-size: 19px;
    line-height: 1;
  }
  .contact-list li {
    position: absolute;
    left: 0;
    white-space: nowrap;
    transform: translateY(-50%);
  }
  .contact--phone { top: 113px; }
  .contact--email { top: 151px; }
  .contact--social { top: 192px; }
  .contact--web { top: 231px; }
  .contact--address { top: 284px; line-height: 27px; }
</style>
</head>
<body>

  <section class="card card--front" aria-label="Business card front">
    <div class="brand">
      <span class="brand__square" aria-hidden="true"></span>
      <span class="brand__name">Maison Verlaine</span>
    </div>
    <div class="front__gold-band"></div>
    <div class="front__dark-band"></div>
  </section>

  <section class="card card--back" aria-label="Business card back">
    <div class="brand">
      <span class="brand__square" aria-hidden="true"></span>
      <span class="brand__name">Maison Verlaine</span>
    </div>

    <div class="back__dark-panel"></div>

    <div class="icon-rail" aria-hidden="true">
      <svg class="icon icon--phone" viewBox="0 0 24 24">
        <path fill="#111" d="M6.6 10.8a15.2 15.2 0 0 0 6.6 6.6l2.2-2.2c.3-.3.7-.4 1-.2 1.1.4 2.3.6 3.6.6.6 0 1 .4 1 1V20c0 .6-.4 1-1 1A17 17 0 0 1 3 4c0-.6.4-1 1-1h3.5c.6 0 1 .4 1 1 0 1.3.2 2.5.6 3.6.1.3 0 .7-.2 1z"/>
      </svg>
      <svg class="icon icon--mail" viewBox="0 0 24 24">
        <rect x="2" y="5" width="20" height="14" fill="none" stroke="#111" stroke-width="2"/>
        <path d="M2 5l10 8 10-8M2 19l7.5-7M22 19l-7.5-7" fill="none" stroke="#111" stroke-width="1.6"/>
      </svg>
      <svg class="icon icon--social" viewBox="0 0 24 24">
        <circle cx="12" cy="12" r="9" fill="none" stroke="#111" stroke-width="2"/>
      </svg>
      <svg class="icon icon--link" viewBox="0 0 24 24">
        <g fill="none" stroke="#111" stroke-width="2.2" stroke-linecap="round">
          <path d="M10 14a4 4 0 0 0 5.7 0l3.5-3.5a4 4 0 0 0-5.7-5.7L12 6.3"/>
          <path d="M14 10a4 4 0 0 0-5.7 0l-3.5 3.5a4 4 0 0 0 5.7 5.7L12 17.7"/>
        </g>
      </svg>
      <svg class="icon icon--pin" viewBox="0 0 24 24">
        <path fill="#111" d="M12 2a7 7 0 0 0-7 7c0 5 7 13 7 13s7-8 7-13a7 7 0 0 0-7-7zm0 10a3 3 0 1 1 0-6 3 3 0 0 1 0 6z"/>
      </svg>
    </div>

    <ul class="contact-list">
      <li class="contact--phone">514 286 5937</li>
      <li class="contact--email">info@maisonverlaine.example</li>
      <li class="contact--social">@Maisonverlaine</li>
      <li class="contact--web">www.maisonverlaine.example</li>
      <li class="contact--address">4817 Morneau Boulevard<br>Montreal, QC, K7P4M2</li>
    </ul>
  </section>

</body>
</html>
```